Chiropractic Flyers to be made more up to date

I have used this series of flyers for my own practice. I would like the graphics to be brought up to date and the name of the doctor and the practice, the address, phone number and date to be removed and a blank box inserted in one place on the flyer that other chiropractors could use to personalize the flyers for their practice. On some of the flyers, this information is in several places. I'd like to have it all in one space so that it would be easy for the doctor to add it in their practice. They all need to be bright and colorful with catchy graphics.

```html
<!DOCTYPE html>
<html lang="en">
<head>
<meta charset="utf-8">
<title>Spring into Health</title>
<link rel="stylesheet" href="https://fonts.googleapis.com/css2?family=Titan+One&family=Nunito:wght@400;800&display=swap">
<style>
  :root {
    --pink: #e8147f;
    --pink-light: #f27ab8;
    --green: #1fa21c;
    --green-dark: #0e6e12;
    --cream: #eef0d6;
    --white: #ffffff;
  }
  html, body { margin: 0; padding: 0; overflow: hidden; }
  .flyer {
    position: relative;
    width: 927px;
    height: 1200px;
    overflow: hidden;
    font-family: "Nunito", sans-serif;
  }
  .backdrop {
    position: absolute; inset: 0;
    background:
      radial-gradient(ellipse 260px 200px at 250px 150px, #e0508f 0%, rgba(224,80,143,0.6) 45%, rgba(224,80,143,0) 100%),
      radial-gradient(ellipse 90px 110px at 20px 320px, rgba(230,90,140,0.8), rgba(230,90,140,0)),
      radial-gradient(ellipse 110px 120px at 880px 360px, rgba(235,90,140,0.75), rgba(235,90,140,0)),
      radial-gradient(ellipse 90px 140px at 20px 880px, rgba(230,80,130,0.6), rgba(230,80,130,0)),
      radial-gradient(ellipse 120px 160px at 900px 900px, rgba(210,190,120,0.5), rgba(210,190,120,0)),
      radial-gradient(ellipse 300px 220px at 100px 180px, rgba(150,200,110,0.7), rgba(150,200,110,0)),
      linear-gradient(180deg, #d8e6b8 0%, var(--cream) 40%, #eef0d2 65%, #dfe6b4 100%);
  }
  .badge {
    position: absolute;
    left: 527px; top: -105px;
    width: 412px; height: 412px;
    border-radius: 50%;
    background: radial-gradient(circle at 45% 40%, #f0278f, var(--pink) 70%, #c80e6c);
    border: 3px solid var(--white);
    box-shadow: 0 4px 10px rgba(0,0,0,0.25);
  }
  .badge-text {
    position: absolute;
    left: 590px; top: 26px; width: 310px;
    text-align: center;
    color: var(--white);
    font-family: "Titan One", sans-serif;
    text-shadow: 2px 3px 3px rgba(0,0,0,0.35);
    margin: 0;
  }
  .badge-free { display: block; font-size: 86px; line-height: 1; letter-spacing: 2px; }
  .badge-sub { display: block; font-size: 38px; line-height: 54px; margin-top: 4px; letter-spacing: 1px; }
  .title {
    position: absolute; left: 0; top: 0;
    width: 927px; height: 720px;
    margin: 0;
  }
  .title text { font-family: "Nunito", sans-serif; }
  .title-spring, .title-health { font-weight: 800; filter: drop-shadow(2px 3px 2px rgba(0,0,0,0.3)); }
  .title-spring { fill: var(--green); }
  .title-into { fill: var(--pink-light); font-weight: 400; }
  .title-health { fill: var(--pink); }
  .details-tabs { position: absolute; left: 90px; top: 730px; }
  .details-box {
    position: absolute;
    left: 135px; top: 732px;
    width: 638px; height: 280px;
    background: linear-gradient(180deg, #e6e6e6 0%, var(--white) 12%, var(--white) 88%, #dcdcdc 100%);
    box-shadow: 0 3px 8px rgba(0,0,0,0.2);
  }
  .services-band {
    position: absolute;
    left: 0; top: 1015px; width: 927px; height: 130px;
    background: linear-gradient(90deg, var(--green-dark), #1a7d1f 50%, var(--green-dark));
    border-top: 2px solid var(--white);
    border-bottom: 2px solid var(--white);
    color: var(--white);
    text-align: center;
    font-family: "Nunito", sans-serif;
    font-size: 45px;
    line-height: 56px;
    padding-top: 8px;
    box-sizing: border-box;
  }
  .services-band p { margin: 0; white-space: nowrap; }
  .meadow {
    position: absolute;
    left: 0; top: 1148px; width: 927px; height: 52px;
    background: linear-gradient(90deg, #b04aa0, #4f7a3a 20%, #e0603a 35%, #c45ab0 55%, #6a8a40 70%, #e06a40 85%, #a050b0);
  }
</style>
</head>
<body>
<div class="flyer">
  <div class="backdrop" role="img" aria-label="Pink blossom branch over a softly blurred spring garden"></div>

  <div class="badge"></div>
  <p class="badge-text">
    <span class="badge-free">FREE!</span>
    <span class="badge-sub">fun for<br>the whole<br>family !</span>
  </p>

  <svg class="title" viewBox="0 0 927 720" role="heading" aria-level="1" aria-label="spring into health">
    <text class="title-spring" x="118" y="548" font-size="178" textLength="494" lengthAdjust="spacingAndGlyphs">spring</text>
    <text class="title-into" x="243" y="650" font-size="68" textLength="123" lengthAdjust="spacingAndGlyphs">into</text>
    <text class="title-health" x="378" y="688" font-size="182" textLength="464" lengthAdjust="spacingAndGlyphs">health</text>
  </svg>

  <svg class="details-tabs" width="730" height="110" viewBox="0 0 730 110">
    <polygon points="45,0 45,108 0,108" fill="#1a8a1c"/>
    <polygon points="683,0 683,108 728,108" fill="#1a8a1c"/>
  </svg>
  <div class="details-box" aria-label="Space for practice name, address, phone and date"></div>

  <div class="services-band">
    <p>free: fitness demonstrations</p>
    <p>health screenings, spinal exams</p>
  </div>

  <div class="meadow" role="img" aria-label="Strip of colourful garden flowers"></div>
</div>
</body>
</html>
```